PSD website for property company

Please read the brief thoroughly.

We are looking for a new website for a property group that does property acquisitions, property development and property management.
They buy, build and lease core inner city industrial assets in Sydney, Australia.
They also invest in residential developments.

Site menu
- Home page
- Property – sub menus include – Leasing ; Projects ; Investments ; Property Management
- Capital and finance
- About
- Contact

They like this website
https://www.verlo.com.au/

They want the site to be clean, modern and bold.
They like few colors, even black and white is OK to submit

They have a logo and style guide and useable images here:
http://www.kumet.net/temp/PelorisWeb2019.zip
The zip file is also attached to this project.
We have supplied some images to give you an idea, but we will also require you to provide at least 3 extra images from stock photos.
Use your imagination.

I am expecting a lot of similar designs, so be aware the photos you choose will be really important.
They want really 3 good stock photos used and supplied without charge.
Please not too generic, I repeat the quality of the photos is important.
You may provide several photos (but not in multiple submissions please) and we will choose the best three to be provided.

The winner will be selected on a single home page design and required to provide;
All photos use in original format without charge
A second ‘standard page’ template design based on the winning home page design

```html
<!DOCTYPE html>
<html lang="en">
<head>
<meta charset="utf-8">
<title>Peloris — Property Group</title>
<link href="https://fonts.googleapis.com/css2?family=Jost:wght@300;400;500;600;700&display=swap" rel="stylesheet">
<style>
:root{
  --blue:#3572ef;
  --red:#ff4d4d;
  --coral:#ff8c69;
  --green:#1fc58a;
  --navy:#0b1a33;
  --ink:#0f1c33;
  --page:#f2f7fe;
  --white:#ffffff;
  --muted:#8a93a6;
}
*{box-sizing:border-box;margin:0;padding:0}
html,body{width:1200px;height:4152px;overflow:hidden}
body{position:relative;background:var(--page);font-family:"Jost",sans-serif;color:var(--ink)}
.abs{position:absolute}
.hero{left:0;top:0;width:1200px;height:662px;background:var(--blue)}
.brand{font-weight:600;font-size:18px;color:var(--white);left:190px;top:35px}
.nav a{position:absolute;top:40px;font-size:12px;font-weight:500;color:var(--white);text-decoration:none;white-space:nowrap}
.hero-title{left:190px;top:268px;font-size:64px;font-weight:700;color:var(--white);letter-spacing:1px;line-height:1}
.hero-sub{left:190px;top:362px;font-size:11.5px;line-height:16px;color:var(--white);font-weight:300}
.btn{display:flex;align-items:center;justify-content:center;background:var(--red);color:var(--white);font-size:11.5px;font-weight:600;letter-spacing:.8px}
.hero-frame{left:608px;top:197px;width:402px;height:465px;background:var(--red)}
.photo{position:absolute}
.about-card{left:190px;top:584px;width:786px;height:553px;background:var(--white)}
.kicker{font-size:26px;font-weight:300;color:var(--ink);line-height:1}
.heading{font-size:54px;font-weight:700;color:var(--ink);line-height:1}
.body{font-size:11px;line-height:16.5px;color:var(--ink)}
.ghost{left:500px;top:790px;font-size:150px;font-weight:700;color:#f4f6fa;line-height:1;letter-spacing:2px}
.more{display:flex;align-items:center;height:30px;width:140px}
.more .sq{position:absolute;left:0;top:0;width:30px;height:30px;background:var(--red)}
.more span.t{position:relative;margin-left:14px;font-size:10.5px;font-weight:500;color:var(--ink)}
.more .ln{position:relative;margin-left:8px;width:46px;height:1px;background:var(--ink)}
.icon-box{width:74px;height:74px;border:6px solid;background:var(--white);display:flex;align-items:center;justify-content:center}
.svc-title{font-size:17px;font-weight:600;color:var(--ink)}
.svc-desc{font-size:11px;line-height:21px;color:var(--ink)}
.feature-band{left:0;top:1879px;width:589px;height:524px;background:var(--blue)}
.card{left:386px;top:1971px;width:262px;height:339px;background:var(--white);box-shadow:0 10px 24px rgba(11,26,51,.18)}
.card-cap{left:15px;top:300px;font-size:13.5px;font-weight:600;color:var(--ink)}
.arrow-btn{width:52px;height:51px;border:1px solid rgba(255,255,255,.8);display:flex;align-items:center;justify-content:center}
.form-card{left:271px;top:3363px;width:660px;height:408px;background:var(--white)}
.field{position:absolute;border-bottom:1px solid #2a3550;font-size:11px;color:#59627a;padding-bottom:6px}
.footer{left:0;top:3855px;width:1200px;height:297px;background:var(--navy);color:var(--white)}
.foot-h{font-size:14px;font-weight:600}
.foot-l{font-size:11px;line-height:27px;font-weight:400}
</style>
</head>
<body>

<!-- Hero -->
<section class="abs hero"></section>
<div class="abs brand">Peloris</div>
<nav class="nav">
  <a style="left:597px;font-weight:700">Home</a>
  <a style="left:666px">Property</a>
  <a style="left:752px">Capital and Finance</a>
  <a style="left:898px">About</a>
  <a style="left:969px">Contact</a>
</nav>
<h1 class="abs hero-title">PELORIS</h1>
<p class="abs hero-sub">Family owned and operated,&nbsp; community orientated.<br>Putting 45 years of local experience to work for the Inner West</p>
<a class="abs btn" style="left:190px;top:423px;width:149px;height:51px">GET STARTED</a>
<div class="abs hero-frame"></div>
<div class="photo" role="img" aria-label="Timber-clad gabled apartment building against a pale blue sky" style="left:642px;top:231px;width:334px;height:353px;background:linear-gradient(180deg,#bcdde6 0%,#b3d2dc 40%,#9a7a5e 62%,#b5705a 100%)"></div>

<!-- About -->
<section class="abs about-card"></section>
<div class="abs ghost">PELORIS</div>
<div class="abs" style="left:234px;top:694px;width:250px;height:356px;background:var(--coral)"></div>
<div class="photo" role="img" aria-label="Looking up at a white and ochre tiled apartment tower under blue sky" style="left:250px;top:710px;width:218px;height:324px;background:linear-gradient(160deg,#4fa6dc 0%,#8cc8ea 35%,#f2efe8 55%,#c99a5a 80%,#e9e5dd 100%)"></div>
<p class="abs kicker" style="left:532px;top:726px">Who are</p>
<h2 class="abs heading" style="left:532px;top:763px">PELORIS</h2>
<p class="abs body" style="left:532px;top:846px;width:380px">When Stavros Peloris first stepped off the boat and on to Australia's shores, he dreamt of building a long and prosperous life for his family for many generations to come.</p>
<p class="abs body" style="left:532px;top:911px;width:380px">Accustomed to working with his hands, he soon found employment building one of Australia's most iconic projects, the Hydro</p>
<div class="abs more" style="left:532px;top:987px"><i class="sq"></i><span class="t">View More</span><i class="ln"></i></div>

<!-- Services -->
<p class="abs kicker" style="left:190px;top:1289px">Services</p>
<h2 class="abs heading" style="left:190px;top:1333px">We Provide</h2>

<div class="abs icon-box" style="left:190px;top:1463px;border-color:var(--coral)">
  <svg width="24" height="22" viewBox="0 0 24 22"><path d="M2 3h4l3 11h11l3-8H8" fill="none" stroke="#ff6a5a" stroke-width="2.4"/><circle cx="10" cy="19" r="2" fill="#ff6a5a"/><circle cx="19" cy="19" r="2" fill="#ff6a5a"/></svg>
</div>
<div class="abs icon-box" style="left:503px;top:1463px;border-color:var(--green)">
  <svg width="24" height="22" viewBox="0 0 24 22"><path d="M3 21V8l7-4v17M10 21V2l8 4v15M1 21h22" fill="var(--green)" stroke="var(--green)" stroke-width="1.5"/></svg>
</div>
<div class="abs icon-box" style="left:816px;top:1463px;border-color:var(--blue)">
  <svg width="22" height="22" viewBox="0 0 22 22"><path d="M2 10L11 2l9 8v10H2z" fill="var(--blue)"/><circle cx="11" cy="13" r="3" fill="#fff"/></svg>
</div>

<h3 class="abs svc-title" style="left:190px;top:1569px">Property Acquisitions</h3>
<h3 class="abs svc-title" style="left:503px;top:1569px">Property Development</h3>
<h3 class="abs svc-title" style="left:816px;top:1569px">Property Management</h3>
<p class="abs svc-desc" style="left:190px;top:1605px;width:190px">Lorem ipsum dolor sit amet,<br>consetetur sadipscing elitr, sed<br>diam nonumy eirmod tempor</p>
<p class="abs svc-desc" style="left:503px;top:1605px;width:190px">Lorem ipsum dolor sit amet,<br>consetetur sadipscing elitr, sed<br>diam nonumy eirmod tempor</p>
<p class="abs svc-desc" style="left:816px;top:1605px;width:190px">Lorem ipsum dolor sit amet,<br>consetetur sadipscing elitr, sed<br>diam nonumy eirmod tempor</p>
<div class="abs more" style="left:190px;top:1704px"><i class="sq"></i><span class="t">View More</span><i class="ln"></i></div>
<div class="abs more" style="left:503px;top:1704px"><i class="sq"></i><span class="t">View More</span><i class="ln"></i></div>
<div class="abs more" style="left:816px;top:1704px"><i class="sq"></i><span class="t">View More</span><i class="ln"></i></div>

<!-- Featured project -->
<section class="abs feature-band"></section>
<div class="photo" role="img" aria-label="Glass and concrete office building corner" style="left:34px;top:2123px;width:145px;height:187px;background:linear-gradient(180deg,#b9d3e6 0%,#d6d4cf 45%,#3f6e86 70%,#c9c6bf 100%)"></div>
<div class="photo" role="img" aria-label="Cream rendered house gable with brown windows" style="left:208px;top:2123px;width:145px;height:187px;background:linear-gradient(180deg,#cfe1ee 0%,#8a4f3a 22%,#f2dcb8 40%,#ead2a8 100%)"></div>
<section class="abs card">
  <div class="photo" role="img" aria-label="Curved white modernist building with circular balconies against blue sky" style="left:0;top:0;width:262px;height:287px;background:linear-gradient(160deg,#3f8fd8 0%,#8fc1ea 40%,#f0ece3 60%,#d9d2c4 100%)"></div>
  <p class="abs card-cap">Marlow St – Creative Arts Precinct</p>
</section>
<div class="abs arrow-btn" style="left:452px;top:2331px"><svg width="6" height="8" viewBox="0 0 6 8"><path d="M5 1L2 4l3 3" fill="none" stroke="#fff" stroke-width="1.2"/></svg></div>
<div class="abs arrow-btn" style="left:516px;top:2331px"><svg width="6" height="8" viewBox="0 0 6 8"><path d="M1 1l3 3-3 3" fill="none" stroke="#fff" stroke-width="1.2"/></svg></div>

<p class="abs" style="left:705px;top:1978px;font-size:17px;font-weight:400">Featured Project</p>
<h2 class="abs" style="left:705px;top:2012px;font-size:37px;font-weight:600;line-height:50px">Marlow St – Creative<br>Arts Precinct</h2>
<p class="abs body" style="left:705px;top:2121px;width:315px;line-height:21px">Lorem ipsum dolor sit amet, consetetur sadipscing elitr, sed diam nonumy eirmod tempor invidunt ut labore et dolore magna aliquyam erat, sed diam voluptua. At vero eos et accusam et justo duo dolores et ea rebum. Stet clita kasd gubergren,</p>
<div class="abs more" style="left:705px;top:2253px"><i class="sq"></i><span class="t">View More</span><i class="ln"></i></div>

<!-- Community -->
<p class="abs kicker" style="left:190px;top:2640px">Our Relationship With</p>
<h2 class="abs heading" style="left:190px;top:2684px">The Community</h2>
<p class="abs body" style="left:190px;top:2768px;width:375px;line-height:21px">We have been a part of the Inner West community for more than 50 years, and we plan to remain a part of the community for many years to come. We believe in building communities, not just buildings, and delivering local employment opportunities, so business and people can thrive together.</p>
<div class="abs more" style="left:190px;top:2906px"><i class="sq"></i><span class="t">View More</span><i class="ln"></i></div>
<div class="abs" style="left:656px;top:2578px;width:300px;height:412px;background:var(--green)"></div>
<div class="photo" role="img" aria-label="Smiling woman with red curly hair in a navy floral dress against a grey block wall" style="left:674px;top:2597px;width:263px;height:374px;background:linear-gradient(180deg,#a9adb0 0%,#9ea3a6 35%,#2b3a5e 70%,#1f2c4a 100%)"></div>

<!-- Contact -->
<p class="abs" style="left:0;top:3170px;width:1200px;text-align:center;font-size:25px;font-weight:300">Have a Question ?</p>
<h2 class="abs heading" style="left:0;top:3214px;width:1200px;text-align:center">Contact Us</h2>
<div class="abs" style="left:0;top:3323px;width:1200px;height:532px;background:linear-gradient(180deg,#edf2fb 0%,#e6edf8 100%)"></div>
<section class="abs form-card">
  <label class="field" style="left:58px;top:59px;width:256px">First Name</label>
  <label class="field" style="left:344px;top:59px;width:256px">Last Name</label>
  <label class="field" style="left:58px;top:121px;width:256px">E-mail</label>
  <label class="field" style="left:344px;top:121px;width:256px">Phone</label>
  <label class="abs" style="left:58px;top:176px;font-size:11px;color:#59627a">Your Massage</label>
  <i class="abs" style="left:63px;top:281px;width:537px;height:1px;background:#2a3550"></i>
  <a class="abs btn" style="left:63px;top:320px;width:187px;height:43px">Submit Now</a>
</section>

<!-- Footer -->
<footer class="abs footer">
  <div class="abs" style="left:190px;top:65px;font-size:20px;font-weight:600">Peloris</div>
  <p class="abs" style="left:190px;top:112px;width:270px;font-size:11px;line-height:15px">Family owned and operated,&nbsp; community orientated.Putting 45 years of local experience to work for the Inner West</p>
  <div class="abs" style="left:190px;top:179px;display:flex;gap:19px">
    <i style="width:14px;height:14px;border:1.5px solid #fff;border-radius:50%"></i>
    <i style="width:14px;height:14px;border:1.5px solid #fff;border-radius:50%"></i>
    <i style="width:14px;height:14px;border:1.5px solid #fff;border-radius:50%"></i>
    <i style="width:14px;height:14px;border:1.5px solid #fff;border-radius:50%"></i>
  </div>
  <p class="abs foot-h" style="left:566px;top:62px">Quick Links</p>
  <p class="abs foot-l" style="left:566px;top:99px">Property<br>Capital and Finance<br>About<br>Contact</p>
  <p class="abs foot-h" style="left:719px;top:62px">Information</p>
  <p class="abs foot-l" style="left:719px;top:99px">Terms &amp; Condition<br>Privacy &amp; Policy<br>Support</p>
  <p class="abs foot-h" style="left:868px;top:62px">Contact us</p>
  <p class="abs foot-l" style="left:868px;top:99px">Phone : (02) 9000 4127<br>Email: hello@peloris.example</p>
  <p class="abs" style="left:185px;top:259px;font-size:11px">© Copyright 2018 - 2019&nbsp; |&nbsp;&nbsp; All Rights Reserved</p>
</footer>

</body>
</html>
```